Service Menu refresh 2018 Update of menu pricing

We currently have service menus as attached. We will be updating our look via our homepage image, our service menu and our in-house beverage and treatment menu.
We are a natural and sustainable hair salon group and moving more towards head spa which consists of treatments, beauty, tanning as well as your traditional hair services. Our imagery needs to reflect our efforts in spa treatments in the hair and scalp area and use natural materials and colours reflecting sustainability.
Velin is the brand we stock and promote.

Target Market(s)

Men or women interesting in personal maintenance with natural and organic products and using sustainable practises

Industry/Entity Type

Hair And Beauty

Font styles to use
Sans Serif
Other font styles liked:
• Arial or Helvetica

Colors
9acb3c
abd037
cadf82
ffffff

Requirements
Must have
• Name on the front cover, locations on back cover
Nice to have
• Prestige feel, reflect male and female clients
Should not have
• Bold artificial writing or any type of cartoon images.
• Same images as existing menu.

```html
<!DOCTYPE html>
<html lang="en">
<head>
<meta charset="utf-8">
<title>Verdane Hair Studios – Service Menu</title>
<link rel="stylesheet" href="https://fonts.googleapis.com/css2?family=Arimo:ital,wght@0,400;0,700;1,400;1,700&display=swap">
<style>
:root{
  --green:#6cbf2a;
  --green-soft:#9acb3c;
  --green-pale:#cadf82;
  --ink:#1b1b1b;
  --muted:#555;
  --paper:#ffffff;
  --paper-grey:#f1f2ef;
  --bg:#e6e7e4;
}
*{box-sizing:border-box;margin:0;padding:0}
html,body{width:816px;height:1200px;overflow:hidden}
body{background:var(--bg);font-family:Arimo,Arial,Helvetica,sans-serif;color:var(--ink);position:relative}
.spread{position:absolute;left:20px;width:776px;height:548px;display:flex;box-shadow:0 6px 18px rgba(0,0,0,.18)}
.spread--cover{top:34px}
.spread--inside{top:618px}
.page{position:relative;width:388px;height:548px;overflow:hidden;background:var(--paper)}
.page--textured{background:linear-gradient(160deg,#f7f7f5 0%,var(--paper-grey) 55%,#fafaf8 100%)}
.corner{position:absolute;width:90px;height:110px;border-color:var(--green);border-style:solid;border-width:0}
.corner--tr{top:26px;right:26px;border-top-width:2px;border-right-width:2px}
.corner--bl{bottom:26px;left:26px;border-bottom-width:2px;border-left-width:2px}
.corner--tl{top:26px;left:26px;border-top-width:2px;border-left-width:2px}
.corner--br{bottom:26px;right:26px;border-bottom-width:2px;border-right-width:2px}

/* back cover */
.locations{position:absolute;top:70px;left:0;right:0;text-align:center}
.location{margin-bottom:26px;font-size:9.5px;line-height:1.3;color:var(--ink)}
.location h3{color:var(--green);font-size:15px;font-weight:700;letter-spacing:.2px;margin-bottom:2px}

/* front cover */
.leaves{position:absolute;background:linear-gradient(135deg,#7fd13a,#55b01e);}
.leaves--top{top:0;right:40px;width:170px;height:78px;border-radius:0 0 60px 90px}
.leaves--bottom{bottom:0;left:60px;width:230px;height:110px;border-radius:90px 110px 0 0}
.brand{position:absolute;top:168px;left:0;right:0;display:flex;align-items:center;justify-content:center;gap:9px}
.brand__dot{width:20px;height:20px;border-radius:50%;background:var(--green)}
.brand__name{font-size:22px;font-weight:700;color:var(--ink);letter-spacing:.3px}
.tagline{position:absolute;top:226px;left:0;right:0;text-align:center;font-weight:700;font-size:19px;line-height:1.22;color:var(--ink)}
.tagline .accent{color:var(--green)}

/* inside */
.inside-page{padding:22px 22px 0 24px}
.pill{display:inline-block;background:var(--green);color:#fff;font-weight:700;font-style:italic;font-size:10.5px;padding:3px 14px 3px 24px;border-radius:0 12px 12px 0;margin:6px 0 4px -24px;text-transform:uppercase}
.sizes{display:flex;justify-content:flex-end;margin:-4px 0 2px}
.size{width:32px;display:flex;justify-content:center}
.size span{width:17px;height:17px;border-radius:50%;background:var(--green);color:#fff;font-weight:700;font-size:9px;display:flex;align-items:center;justify-content:center}
.group{font-size:8.5px;font-weight:700;text-transform:uppercase;margin-top:3px}
.row{display:flex;align-items:flex-end;font-size:8px;line-height:11.5px}
.row__item{white-space:nowrap;font-style:italic}
.row__dots{flex:1;border-bottom:1px dotted #888;margin:0 3px 3px}
.row__price{width:32px;text-align:center;font-weight:700}
.note{font-size:6.5px;color:var(--muted);font-style:italic;margin-top:3px}
.photos{position:absolute;bottom:50px;left:22px;right:22px;display:flex;justify-content:space-between}
.photo{width:160px;height:104px;border:3px solid var(--green);border-radius:12px}
.photo--wash{background:linear-gradient(135deg,#d9d6d2,#b9aaa0 60%,#e9e6e2)}
.photo--barber{background:linear-gradient(135deg,#dfe6df,#8a7a6a 60%,#c9d4c9)}
.photo--cut{background:linear-gradient(135deg,#b7a08c,#6b5344 60%,#cfc4b8)}
.photo--colour{background:linear-gradient(135deg,#e6d6bf,#c29c72 60%,#efe4d4)}
.band{position:absolute;bottom:12px;left:0;right:0;height:12px;background:var(--green)}
.inside-brand{display:flex;align-items:center;gap:7px;margin:10px 0 0 60px}
.inside-brand .brand__dot{width:16px;height:16px}
.inside-brand .brand__name{font-size:16px}
</style>
</head>
<body>

<section class="spread spread--cover">
  <article class="page page--textured back-cover">
    <span class="corner corner--tr"></span>
    <span class="corner corner--bl"></span>
    <div class="locations">
      <div class="location"><h3>ASHVALE</h3>shop 12 ashvale central,<br>Linden Rd, Ashvale<br>+61 (07) 5550 0101<br>ashvale@verdanestudios.example</div>
      <div class="location"><h3>BROOKHURST</h3>shop 47 brookhurst plaza,<br>Marlow road, Brookhurst<br>+61 (07) 5550 0102<br>brookhurst@verdanestudios.example</div>
      <div class="location"><h3>FERNLEIGH</h3>shop 208 fernleigh shopping centre,<br>Quarry Rd, Fernleigh<br>+61 (07) 5550 0103<br>fernleigh@verdanestudios.example</div>
      <div class="location"><h3>LAKEMONT</h3>shop 63 lakemont square,<br>Harbour st, Lakemont<br>+61 (07) 5550 0104<br>lakemont@verdanestudios.example</div>
      <div class="location"><h3>RIVERSIDE HEALTH PRECINCT</h3>Ashgrove st, Riverside, QLD 4999<br>+61 (07) 5550 0105<br>riverside@verdanestudios.example</div>
    </div>
  </article>
  <article class="page page--textured front-cover">
    <div class="leaves leaves--top" role="img" aria-label="Hand-drawn green leaf cluster"></div>
    <span class="corner corner--tl"></span>
    <span class="corner corner--br"></span>
    <div class="brand"><span class="brand__dot"></span><span class="brand__name">Verdane Hair Studios</span></div>
    <p class="tagline">Living a more<br><span class="accent">NATURAL</span> and <span class="accent">ORGANIC</span><br>life is a Philosophy<br>not just a<br><span class="accent">PRODUCT CERTIFICATION</span></p>
    <div class="leaves leaves--bottom" role="img" aria-label="Hand-drawn green leaf cluster"></div>
  </article>
</section>

<section class="spread spread--inside">
  <article class="page inside-page">
    <span class="pill">Cut &amp; Blowdry</span>
    <div class="sizes"><div class="size"><span>S</span></div><div class="size"><span>M</span></div><div class="size"><span>L</span></div><div class="size"><span>X</span></div></div>
    <div class="group">Ladies</div>
    <div class="row"><span class="row__item">fringe</span><span class="row__dots"></span><span class="row__price">$24</span><span class="row__price"></span><span class="row__price"></span><span class="row__price"></span></div>
    <div class="row"><span class="row__item">Trim</span><span class="row__dots"></span><span class="row__price">$77</span><span class="row__price">$88</span><span class="row__price">$99</span><span class="row__price">$110</span></div>
    <div class="row"><span class="row__item">Restyle</span><span class="row__dots"></span><span class="row__price">$85</span><span class="row__price">$95</span><span class="row__price">$105</span><span class="row__price">$120</span></div>
    <div class="group">Mens</div>
    <div class="row"><span class="row__item">Single clipper</span><span class="row__dots"></span><span class="row__price">$25</span><span class="row__price"></span><span class="row__price"></span><span class="row__price"></span></div>
    <div class="row"><span class="row__item">Style cut</span><span class="row__dots"></span><span class="row__price">$35</span><span class="row__price"></span><span class="row__price"></span><span class="row__price"></span></div>
    <div class="group">Children</div>
    <div class="row"><span class="row__item">10 and under</span><span class="row__dots"></span><span class="row__price">$28</span><span class="row__price"></span><span class="row__price"></span><span class="row__price"></span></div>
    <div class="row"><span class="row__item">11-16 Male</span><span class="row__dots"></span><span class="row__price">$42</span><span class="row__price"></span><span class="row__price"></span><span class="row__price"></span></div>
    <div class="row"><span class="row__item">11-16 Female</span><span class="row__dots"></span><span class="row__price">$48</span><span class="row__price"></span><span class="row__price"></span><span class="row__price"></span></div>
    <div class="row"><span class="row__item">add a wash</span><span class="row__dots"></span><span class="row__price">$5</span><span class="row__price"></span><span class="row__price"></span><span class="row__price"></span></div>
    <div class="group">Blowdry</div>
    <div class="row"><span class="row__item">Shampoo &amp; dry off</span><span class="row__dots"></span><span class="row__price">$47</span><span class="row__price">$57</span><span class="row__price">$67</span><span class="row__price">$77</span></div>
    <span class="pill">Treatments</span>
    <div class="row"><span class="row__item">Deep treatment</span><span class="row__dots"></span><span class="row__price">$35</span><span class="row__price"></span><span class="row__price"></span><span class="row__price"></span></div>
    <div class="row"><span class="row__item">Head Spa ritual</span><span class="row__dots"></span><span class="row__price">$65</span><span class="row__price"></span><span class="row__price"></span><span class="row__price"></span></div>
    <span class="pill">Upstyle</span>
    <div class="row"><span class="row__item">45 minutes</span><span class="row__dots"></span><span class="row__price">$85</span><span class="row__price"></span><span class="row__price"></span><span class="row__price"></span></div>
    <div class="row"><span class="row__item">90 minutes</span><span class="row__dots"></span><span class="row__price">$120</span><span class="row__price"></span><span class="row__price"></span><span class="row__price"></span></div>
    <div class="photos">
      <div class="photo photo--wash" role="img" aria-label="Photo of a client relaxing at the basin during a scalp wash"></div>
      <div class="photo photo--barber" role="img" aria-label="Photo of a bearded man having his hair styled"></div>
    </div>
    <div class="band" role="img" aria-label="Green and black striped border band"></div>
  </article>

  <article class="page inside-page">
    <span class="pill">Colour</span>
    <div class="sizes"><div class="size"><span>S</span></div><div class="size"><span>M</span></div><div class="size"><span>L</span></div><div class="size"><span>X</span></div></div>
    <div class="row"><span class="row__item">regrowth</span><span class="row__dots"></span><span class="row__price">$83</span><span class="row__price"></span><span class="row__price"></span><span class="row__price"></span></div>
    <div class="row"><span class="row__item">full color tint</span><span class="row__dots"></span><span class="row__price">$125</span><span class="row__price">$145</span><span class="row__price">$165</span><span class="row__price">$185</span></div>
    <div class="row"><span class="row__item">regrowth lightening*</span><span class="row__dots"></span><span class="row__price">$165</span><span class="row__price">$189</span><span class="row__price">$209</span><span class="row__price">$229</span></div>
    <div class="row"><span class="row__item">balayage/ombre*</span><span class="row__dots"></span><span class="row__price">$275</span><span class="row__price">$375</span><span class="row__price">$475</span><span class="row__price"></span></div>
    <span class="pill">Herbal</span>
    <div class="row"><span class="row__item">regrowth</span><span class="row__dots"></span><span class="row__price">$99</span><span class="row__price"></span><span class="row__price"></span><span class="row__price"></span></div>
    <div class="row"><span class="row__item">full color tint</span><span class="row__dots"></span><span class="row__price">$155</span><span class="row__price">$175</span><span class="row__price">$195</span><span class="row__price">$205</span></div>
    <span class="pill">Foils*</span>
    <div class="row"><span class="row__item">single*</span><span class="row__dots"></span><span class="row__price">$11</span><span class="row__price">$13</span><span class="row__price">$17</span><span class="row__price">$22</span></div>
    <div class="row"><span class="row__item">1/4 head</span><span class="row__dots"></span><span class="row__price">$135</span><span class="row__price">$155</span><span class="row__price">$175</span><span class="row__price">$195</span></div>
    <div class="row"><span class="row__item">1/2 head</span><span class="row__dots"></span><span class="row__price">$185</span><span class="row__price">$205</span><span class="row__price">$235</span><span class="row__price">$265</span></div>
    <div class="row"><span class="row__item">full head</span><span class="row__dots"></span><span class="row__price">$235</span><span class="row__price">$265</span><span class="row__price">$315</span><span class="row__price">$355</span></div>
    <span class="pill">Straight</span>
    <div class="row"><span class="row__item">keratin straightening system</span><span class="row__dots"></span><span class="row__price">$235</span><span class="row__price">$265</span><span class="row__price">$315</span><span class="row__price">$355</span></div>
    <p class="note">* Includes colour match &amp; toner &nbsp;&nbsp; * Minimum 6 foils without colour &nbsp;&nbsp; * Minimum charge on a sunday is $40</p>
    <div class="inside-brand"><span class="brand__dot"></span><span class="brand__name">Verdane Hair Studios</span></div>
    <div class="photos">
      <div class="photo photo--cut" role="img" aria-label="Photo of a stylist cutting a man's hair"></div>
      <div class="photo photo--colour" role="img" aria-label="Photo of a stylist colouring a woman's hair"></div>
    </div>
    <div class="band" role="img" aria-label="Green and black striped border band"></div>
  </article>
</section>

</body>
</html>
```